German Webagency needs fresh modern Design

Our website is 4 years old. We need an fresh modern website. All pics we used before are from customers or handmade by us. the new website should be clear with nice handling. please dont copy something from template websites. it would be great if you can surprise us with something great. its our first project here. don´t worry if i make a mistake in responding or briefing. after 20 years you can´t see the works of your own "designer" so we hope for help :-)
our existing site: www.korvanetz.de
Target Market(s)
small and middle sized companys in germany
Number of Pages Required
4 page
Font styles to use
Colors
Designer to choose colors to be used in the design.
Requirements
Must have
- Responsive (sure we code it)
- Modern and big Font ..Headlines and Slider
- innovative..if you know something new..feel free to show
Nice to have
- the site with our works/refences should look great and later easy to handle when we code it or use wp.
- we like black and grey but if you have better ideas also feel free
Should not have
- a cup of coffe..laptop.. a pencil a handwritten font
- dont copy and modify templates from know websites..bad style

```html
<!DOCTYPE html>
<html lang="en">
<head>
<meta charset="utf-8">
<title>korvanetz.de – German Best Webagency</title>
<link rel="stylesheet" href="https://fonts.googleapis.com/css2?family=Open+Sans:ital,wght@0,400;0,600;0,700;1,400&display=swap">
<style>
  :root {
    --blue: #3d8fe0;
    --blue-light: #55adf3;
    --blue-deep: #2f79cf;
    --ink: #333a44;
    --muted: #555d66;
    --orange: #f7941d;
    --orange-light: #fdb023;
    --purple: #6c5ce0;
    --purple-light: #a68cf2;
    --teal: #8fd3ec;
    --card-ink: #4a5bd4;
    --line: #d7dbe0;
    --field: #eeeeee;
    --white: #ffffff;
  }
  * { box-sizing: border-box; margin: 0; padding: 0; }
  html, body { width: 1200px; height: 3403px; overflow: hidden; }
  body { position: relative; font-family: 'Open Sans', Arial, sans-serif; color: var(--ink); background: var(--white); }
  .abs { position: absolute; }

  /* Hero */
  .hero { position: absolute; left: 0; top: 0; width: 1200px; height: 640px;
    background: linear-gradient(120deg, var(--blue-light) 0%, var(--blue) 55%, var(--blue-deep) 100%); overflow: hidden; }
  .hero-wave { position: absolute; left: 0; bottom: 0; width: 1200px; height: 110px; }
  .brand { position: absolute; left: 100px; top: 34px; font-size: 34px; font-weight: 700; color: var(--white); letter-spacing: -0.5px; display: flex; align-items: center; gap: 10px; }
  .brand-dot { width: 14px; height: 14px; border-radius: 50%; background: var(--white); }
  .login { position: absolute; top: 30px; height: 38px; border: 2px solid var(--white); color: var(--white); font-size: 12px; line-height: 34px; padding: 0 12px; text-transform: uppercase; }
  .login-business { left: 847px; }
  .login-consumer { left: 980px; }
  .nav { position: absolute; right: 160px; top: 100px; display: flex; gap: 21px; list-style: none; }
  .nav li { font-size: 11.5px; color: var(--white); text-transform: uppercase; padding-bottom: 6px; }
  .nav li.active { border-bottom: 2px solid var(--white); }
  .hero-title { position: absolute; left: 100px; top: 214px; font-size: 34px; line-height: 40px; font-weight: 400; color: var(--white); text-transform: uppercase; }
  .hero-text { position: absolute; left: 100px; top: 306px; width: 360px; font-size: 15.5px; line-height: 23px; color: var(--white); }
  .btn { display: block; background: linear-gradient(180deg, var(--orange-light), var(--orange)); color: var(--white); text-transform: uppercase; font-size: 11.5px; text-align: center; }
  .hero-btn { position: absolute; left: 100px; top: 398px; width: 122px; height: 36px; line-height: 36px; }
  .hero-visual { position: absolute; left: 522px; top: 278px; width: 496px; height: 334px;
    background: linear-gradient(160deg, #f4f8fd, #dde9f8); border-radius: 10px 10px 4px 4px; }

  /* Section headings */
  .heading { position: absolute; left: 0; width: 1200px; text-align: center; font-size: 27px; font-weight: 400; text-transform: uppercase; }
  .rule { position: absolute; left: 498px; width: 204px; height: 3px; background: var(--line); }
  .rule::after { content: ""; position: absolute; left: 72px; top: 0; width: 60px; height: 3px; background: var(--blue); }
  .on-blue { color: var(--white); }
  .rule.on-blue { background: rgba(255,255,255,0.55); }
  .rule.on-blue::after { background: var(--white); }

  /* What we do */
  .about-text { position: absolute; left: 100px; top: 848px; width: 480px; font-size: 12.5px; line-height: 21px; color: var(--muted); }
  .about-text p { margin-bottom: 16px; }
  .about-visual { position: absolute; left: 660px; top: 805px; width: 340px; height: 352px; border-radius: 50%;
    background: radial-gradient(circle, #eef3fa 0%, #f8fafd 60%, var(--white) 75%); }

  /* How it works */
  .process { position: absolute; left: 0; top: 1236px; width: 1200px; height: 630px;
    background: linear-gradient(160deg, #4b9de8 0%, var(--blue) 50%, #2d76c9 100%); }
  .process-card { position: absolute; width: 268px; height: 177px; background: var(--white); text-align: center; }
  .process-card svg { position: absolute; left: 89px; top: 20px; }
  .process-card span { position: absolute; left: 0; width: 100%; top: 135px; font-size: 17px; color: var(--card-ink); text-transform: uppercase; }
  .card-purple { background: linear-gradient(90deg, var(--purple-light), var(--purple)); }
  .card-orange { background: linear-gradient(90deg, var(--orange-light), #fa8a1e); }
  .card-teal { background: linear-gradient(90deg, #b9e8f7, var(--teal)); }
  .card-purple span, .card-orange span, .card-teal span { color: var(--white); }

  /* Benefits */
  .benefit-badge { position: absolute; width: 56px; height: 56px; border-radius: 50%; color: var(--white); font-size: 24px; text-align: center; line-height: 56px; box-shadow: 0 4px 10px rgba(0,0,0,0.15); }
  .badge-orange { background: linear-gradient(180deg, var(--orange-light), var(--orange)); }
  .badge-purple { background: linear-gradient(180deg, var(--purple-light), var(--purple)); }
  .benefit-text { position: absolute; left: 184px; width: 400px; font-size: 12.5px; line-height: 21px; color: var(--muted); }
  .benefit-btn { position: absolute; left: 184px; top: 2314px; width: 120px; height: 36px; line-height: 36px; }
  .benefit-visual { position: absolute; left: 612px; top: 2016px; width: 488px; height: 252px;
    background: linear-gradient(160deg, #f4f8fd, #dbe7f7); border-radius: 10px 10px 2px 2px; }

  /* Testimonials */
  .testimonials { position: absolute; left: 0; top: 2427px; width: 1200px; height: 549px;
    background: linear-gradient(160deg, var(--blue-light) 0%, var(--blue) 55%, #3380d2 100%); }
  .quote-card { position: absolute; top: 2626px; width: 250px; height: 272px; background: var(--white); text-align: center; }
  .quote-mark { position: absolute; left: 6px; top: -10px; font-size: 64px; font-weight: 700; color: var(--card-ink); line-height: 1; }
  .avatar { position: absolute; left: 64px; top: -68px; width: 122px; height: 122px; border-radius: 50%; border: 6px solid var(--white); }
  .quote-name { position: absolute; top: 72px; left: 0; width: 100%; font-size: 14px; font-weight: 600; color: #222; }
  .quote-text { position: absolute; top: 102px; left: 20px; width: 210px; font-size: 13px; line-height: 19px; color: #444; }
  .quote-role { position: absolute; left: 0; bottom: 0; width: 100%; height: 36px; line-height: 36px; font-size: 10.5px; font-style: italic; color: var(--white);
    background: linear-gradient(90deg, var(--purple-light), var(--purple)); }
  .slider-arrow { position: absolute; top: 2740px; width: 36px; height: 36px; }

  /* Contact */
  .field { position: absolute; background: var(--field); border: 1px solid #d6d6d6; font-size: 11px; color: #666; padding: 8px 8px; }
  .captcha-code { position: absolute; left: 820px; top: 3238px; font-size: 13px; font-weight: 700; color: #333; letter-spacing: 1px; }
  .send-btn { position: absolute; left: 905px; top: 3230px; width: 129px; height: 36px; line-height: 36px; }

  /* Footer */
  .footer { position: absolute; left: 0; top: 3334px; width: 1200px; height: 69px; background: var(--blue-deep); }
  .footer-copy { position: absolute; left: 100px; top: 26px; font-size: 11.5px; color: var(--white); }
  .social { position: absolute; top: 22px; width: 24px; height: 24px; border: 2px solid var(--white); border-radius: 50%; }
</style>
</head>
<body>

<header class="hero">
  <div class="brand"><span class="brand-dot"></span>korvanetz.de</div>
  <a class="login login-business">Business Login</a>
  <a class="login login-consumer">Consumer Login</a>
  <ul class="nav">
    <li class="active">Home</li><li>What we do</li><li>How it works</li><li>Benefits</li>
    <li>Case study</li><li>Testimonial</li><li>Book a demo</li><li>Contact us</li>
  </ul>
  <h1 class="hero-title">German Best<br>Webagency</h1>
  <p class="hero-text">Lorem Ipsum is simply dummy text of the printing and typesetting industry. Lorem Ipsum has been the industry's standard</p>
  <a class="btn hero-btn">Book a demo</a>
  <div class="hero-visual" role="img" aria-label="Illustration of a desktop monitor and tablet showing UI/UX design and SaaS line drawings"></div>
  <svg class="hero-wave" viewBox="0 0 1200 110" preserveAspectRatio="none">
    <path d="M0,28 C260,-8 560,100 860,70 C1010,55 1120,30 1200,22 L1200,110 L0,110 Z" fill="#ffffff"/>
  </svg>
</header>

<section class="what-we-do">
  <h2 class="heading" style="top:720px;">What we do</h2>
  <div class="rule" style="top:768px;"></div>
  <div class="about-text">
    <p>Lorem Ipsum is simply dummy text of the printing and typesetting industry. Lorem Ipsum has been the industry's standard dummy text ever since the 1500s, when an unknown printer took a galley of type and scrambled it to make.</p>
    <p>a type specimen book. It has survived not only five centuries, but also the leap into electronic typesetting, remaining essentially unchanged. I</p>
    <p>t was popularised in the 1960s with the release of Letraset sheets containing Lorem Ipsum passages, and more recently with desktop publishing software like Aldus PageMaker including versions of Lorem Ipsum.</p>
  </div>
  <div class="about-visual" role="img" aria-label="Illustration of a network of connected people avatars"></div>
</section>

<section class="process">
  <h2 class="heading on-blue" style="top:54px;">How it works</h2>
  <div class="rule on-blue" style="top:100px;"></div>

  <div class="process-card card-purple" style="left:156px; top:147px;">
    <svg width="90" height="90" viewBox="0 0 90 90" fill="none" stroke="#fff" stroke-width="2.5"><circle cx="45" cy="45" r="42"/><rect x="20" y="30" width="50" height="32" rx="4"/><line x1="26" y1="40" x2="40" y2="40"/></svg>
    <span>Allocate cards</span>
  </div>
  <div class="process-card" style="left:465px; top:147px;">
    <svg width="90" height="90" viewBox="0 0 90 90" fill="none" stroke="#4a5bd4" stroke-width="2.5"><circle cx="45" cy="45" r="42"/><path d="M32 22v30M26 46l6 6 6-6M58 52V22M52 28l6-6 6 6"/><circle cx="45" cy="64" r="8"/></svg>
    <span>Direct marketing</span>
  </div>
  <div class="process-card card-orange" style="left:773px; top:147px;">
    <svg width="90" height="90" viewBox="0 0 90 90" fill="none" stroke="#fff" stroke-width="2.5"><circle cx="45" cy="45" r="42"/><path d="M45 20l4 9 10 1-7 7 2 10-9-5-9 5 2-10-7-7 10-1z"/><path d="M20 62h14l10 4h16l8-6"/></svg>
    <span>Rewarding loyalty</span>
  </div>
  <div class="process-card" style="left:156px; top:369px;">
    <svg width="90" height="90" viewBox="0 0 90 90" fill="none" stroke="#1f3f8f" stroke-width="2.5"><circle cx="45" cy="45" r="42"/><rect x="37" y="37" width="16" height="16" fill="#1f3f8f"/><line x1="45" y1="37" x2="45" y2="16"/><line x1="45" y1="53" x2="45" y2="74"/><line x1="37" y1="45" x2="16" y2="45"/><line x1="53" y1="45" x2="74" y2="45"/></svg>
    <span>Collect data</span>
  </div>
  <div class="process-card card-teal" style="left:465px; top:369px;">
    <svg width="90" height="90" viewBox="0 0 90 90" fill="none" stroke="#fff" stroke-width="2.5"><circle cx="45" cy="45" r="42"/><rect x="20" y="24" width="50" height="34" rx="2"/><path d="M26 50l10-10 8 6 12-14 8 6"/><line x1="45" y1="58" x2="45" y2="66"/><line x1="34" y1="66" x2="56" y2="66"/></svg>
    <span>Data analytics</span>
  </div>
  <div class="process-card" style="left:773px; top:369px;">
    <svg width="90" height="90" viewBox="0 0 90 90" fill="none" stroke="#1f3f8f" stroke-width="2.5"><circle cx="45" cy="45" r="42"/><rect x="26" y="50" width="8" height="16"/><rect x="41" y="40" width="8" height="26"/><rect x="56" y="30" width="8" height="36"/><path d="M24 42l16-12 10 6 14-14"/></svg>
    <span>Benefits</span>
  </div>
</section>

<section class="benefits">
  <h2 class="heading" style="top:1930px;">Benefits</h2>
  <div class="rule" style="top:1978px;"></div>
  <div class="benefit-badge badge-orange" style="left:99px; top:2024px;">1</div>
  <p class="benefit-text" style="top:2022px;">Lorem Ipsum is simply dummy text of the printing and typesetting industry. Lorem Ipsum has been the industry's standard dummy text ever since the 1500s, when an unknown printer took a galley of type and scrambled it to make a type specimen book. It has survived not</p>
  <div class="benefit-badge badge-purple" style="left:99px; top:2161px;">2</div>
  <p class="benefit-text" style="top:2156px;">Lorem Ipsum is simply dummy text of the printing and typesetting industry. Lorem Ipsum has been the industry's standard dummy text ever since the 1500s, when an unknown printer took a galley of type and scrambled it to make a type specimen book. It has survived not only five centuries, but also the leap into electronic typesetting, remaining essentially unchanged. It was popularised in the 1960s</p>
  <a class="btn benefit-btn">View more</a>
  <div class="benefit-visual" role="img" aria-label="Illustration of a laptop showing a UI/UX design line drawing"></div>
</section>

<section class="testimonials">
  <h2 class="heading on-blue" style="top:40px;">Testimonials</h2>
  <div class="rule on-blue" style="top:86px;"></div>
</section>
<svg class="slider-arrow" style="left:100px;" viewBox="0 0 36 36" fill="none" stroke="#fff" stroke-width="2"><circle cx="18" cy="18" r="16"/><path d="M21 11l-7 7 7 7"/></svg>
<svg class="slider-arrow" style="left:1064px;" viewBox="0 0 36 36" fill="none" stroke="#fff" stroke-width="2"><circle cx="18" cy="18" r="16"/><path d="M15 11l7 7-7 7"/></svg>

<article class="quote-card" style="left:172px;">
  <div class="quote-mark">“</div>
  <div class="avatar" role="img" aria-label="Portrait photo of a young man" style="background:linear-gradient(160deg,#9fd6e6,#d9a88a);"></div>
  <div class="quote-name">Name Here</div>
  <p class="quote-text">Lorem Ipsum is simply dummy text of the printing and typesetting industry. Lorem Ipsum has been the industry's standard dummy text ever since the 1500s.</p>
  <div class="quote-role">Chief Technology Information Officer</div>
</article>
<article class="quote-card" style="left:476px;">
  <div class="quote-mark">“</div>
  <div class="avatar" role="img" aria-label="Portrait photo of a red-haired woman" style="background:linear-gradient(160deg,#e6e8ea,#d0784e);"></div>
  <div class="quote-name">Name Here</div>
  <p class="quote-text">Lorem Ipsum is simply dummy text of the printing and typesetting industry. Lorem Ipsum has been the industry's standard dummy text ever since the 1500s.</p>
  <div class="quote-role">Professor at Linden University</div>
</article>
<article class="quote-card" style="left:782px;">
  <div class="quote-mark">“</div>
  <div class="avatar" role="img" aria-label="Portrait photo of a blonde woman" style="background:linear-gradient(160deg,#c9dde8,#e0c08a);"></div>
  <div class="quote-name">Name Here</div>
  <p class="quote-text">Lorem Ipsum is simply dummy text of the printing and typesetting industry. Lorem Ipsum has been the industry's standard dummy text ever since the 1500s.</p>
  <div class="quote-role">House wife</div>
</article>

<section class="contact">
  <h2 class="heading" style="top:3020px;">Contact us</h2>
  <div class="rule" style="top:3068px;"></div>
  <div class="field" style="left:152px; top:3116px; width:431px; height:150px;">Message</div>
  <div class="field" style="left:606px; top:3116px; width:428px; height:39px;">Name</div>
  <div class="field" style="left:606px; top:3173px; width:428px; height:38px;">Email</div>
  <div class="field" style="left:606px; top:3230px; width:285px; height:36px;">Type the code shown</div>
  <span class="captcha-code">HG845</span>
  <a class="btn send-btn">Send message</a>
</section>

<footer class="footer">
  <p class="footer-copy">© korvanetz2018. All Rights Reserved. Terms &amp; Conditions</p>
  <span class="social" style="left:992px;"></span>
  <span class="social" style="left:1020px;"></span>
  <span class="social" style="left:1048px;"></span>
  <span class="social" style="left:1076px;"></span>
</footer>

</body>
</html>
```